A modern, fresh introduction to Buddhism

I need a book cover for an A6 sized book to be used both for ebook and hard copy. The author is a young, modern Buddhist teacher of high standing who has written this short intro to Buddhism in an informal Q & As format using modern, accessible language to convey profound and meaningful ideas to the general public. The author is Tibetan, but teaches worldwide and is very personable and dynamic. The cover should portray this and have a fresh yet authentic feel to it (nothing new-agey!). Please see the author's websites www.norvalemtasheteacher.org and www.pwrt.org for reference, but do not feel that the design must align completely with the website designs.

Target Market(s)

General public both in Europe and America and in Asia ranging from teenagers to the elderly. A really broad audience.

Industry/Entity Type

Teacher

Requirements
Must have
• Please include the following text that on the front cover:

A Window onto Stillness

By Drawa Tsomen Lhundrup

Please include the following on the back cover:

Yunor Trenpa Publications (with attached logo above it)
Nice to have
• A simplistic, artistic, and modern look without any traditional religious images.
Should not have
• No buddha images or religious images. I would prefer a more simplistic, modern and artistic look.

```html
<!DOCTYPE html>
<html lang="en">
<head>
<meta charset="utf-8">
<title>A Window onto Stillness — Book Cover</title>
<link rel="stylesheet" href="https://fonts.googleapis.com/css2?family=Oswald:wght@300;400&family=Roboto+Condensed:wght@700&display=swap">
<style>
  :root {
    --backdrop: #5d9095;
    --cover-yellow: #f6c300;
    --cover-magenta: #dc0f78;
    --cover-magenta-deep: #c9086a;
    --cover-orange: #f59a1c;
    --ink-black: #141414;
    --ink-white: #ffffff;
    --band-yellow: #f4c20d;
    --band-text: #c2105f;
    --author-yellow: #f6c300;
  }
  * { margin: 0; padding: 0; box-sizing: border-box; }
  html, body {
    width: 1200px;
    height: 900px;
    overflow: hidden;
    background: var(--backdrop);
  }
  .stage {
    position: relative;
    width: 1200px;
    height: 900px;
  }
  .book-cover {
    position: absolute;
    left: 290px;
    top: 30px;
    width: 620px;
    height: 840px;
    overflow: hidden;
    background: var(--cover-yellow);
  }
  .cover-artwork {
    position: absolute;
    inset: 0;
    background:
      radial-gradient(ellipse 40% 35% at 88% 28%, var(--cover-orange) 0%, rgba(245,154,28,0) 100%),
      linear-gradient(105deg,
        var(--cover-yellow) 0%,
        var(--cover-yellow) 12%,
        var(--cover-magenta) 38%,
        var(--cover-magenta-deep) 62%,
        var(--cover-magenta) 80%,
        var(--cover-yellow) 100%);
  }
  .cover-text {
    position: absolute;
    left: 78px;
    right: 40px;
    top: 296px;
  }
  .title-lead {
    font-family: "Oswald", sans-serif;
    font-weight: 300;
    font-size: 84px;
    line-height: 1;
    letter-spacing: 1px;
    color: var(--ink-black);
    text-transform: uppercase;
  }
  .title-main {
    font-family: "Oswald", sans-serif;
    font-weight: 400;
    font-size: 150px;
    line-height: 1.05;
    color: var(--ink-white);
    margin-top: 2px;
  }
  .subtitle-band {
    display: inline-block;
    margin-top: 30px;
    padding: 3px 10px 2px;
    background: var(--band-yellow);
    font-family: "Roboto Condensed", sans-serif;
    font-weight: 700;
    font-size: 20px;
    letter-spacing: 0.3px;
    color: var(--band-text);
    text-transform: uppercase;
    white-space: nowrap;
  }
  .author-line {
    margin-top: 50px;
    font-family: "Oswald", sans-serif;
    font-weight: 400;
    font-size: 32px;
    color: var(--author-yellow);
  }
  .author-line .by {
    font-size: 22px;
    text-transform: uppercase;
    margin-right: 6px;
  }
</style>
</head>
<body>
  <main class="stage">
    <section class="book-cover">
      <div class="cover-artwork" role="img" aria-label="Photograph of a flowing magenta silk scarf billowing across a warm yellow and orange background"></div>
      <div class="cover-text">
        <h1>
          <span class="title-lead">A Window onto</span><br>
          <span class="title-main">Stillness</span>
        </h1>
        <p class="subtitle-band">A Short Introduction to the Buddha’s Teaching</p>
        <p class="author-line"><span class="by">By</span>Drawa Tsomen Lhundrup</p>
      </div>
    </section>
  </main>
</body>
</html>
```